Website for KiLa online school

I need to get a website for my new online school KiLa Solvander learning. This is a new online school in Norway, offering online courses for expats and other people taking courses in Norwegian and Social Studies, which is mandatory to get permanent residency in Norway. The company needs a simple and functional website that will attract students. It should be easy to use, easy to find information and it has to look professional. The website should have a clean design. simple pictures related to online studies, languages, international connections etc.

Important points:
- I want to use the domain www.solvanderlearn.no and www.solvanderlearn.com in one domain, so if you write www.solvanderlearn.com you will maybe end up in www.solvanderlearn.no/en or something. I own both domains.
- the following words have to be mentioned many times: online learning, norwegian studies, sarn, emt, approved by emt, approved by sarn, norwegian course, study online etc. I guess I will make the text myself? I would like to get some help to make the text in English.
- I want to also have a chatterloom page, but that can come later

I need the following:

- website in both Norwegian and English (customers can click the flag to get English or Norwegian text)
- payment solution with Corda/Bluvex AND coinlyx AND frensa AND invoice - so a payment solution that is easy to use
-clean design
-easy to use
-also adjusted to smartphones and tablets

Logo image is uploaded, but I am waiting for the original files form the designer of the logo. It will come on Monday.

website text added, but this is only a draft. can be used to illustrate

Expats and all people who want to study Norwegian online

Education

1 page

Serif
Sans Serif

fbee3e
e34197
0455a3
9bcb3c
00a990
a64599
333333
ffffff
9d9d9d

• - payment option for corda/bluvex/coinlyx/frensa and invoice. Most important is the corda and bluvex payment
• - two languages: norwegian and english
• - www.solvanderlearn.com should automatically be transeferred to www.solvanderlearn.no/en
• - simple and clean design
• -have to look professional and serious, although colors are used
• pictures related to learning and online studies, as well as language and internatinal relations
• norwegian flags
• too many colors
• too much details

```html
<!DOCTYPE html>
<html lang="en">
<head>
<meta charset="utf-8">
<title>KiLa Solvander learning</title>
<link rel="stylesheet" href="https://fonts.googleapis.com/css2?family=Questrial&family=Open+Sans:wght@400;600;700&display=swap">
<style>
:root{
  --teal:#00a990;
  --teal-soft:#1fb39b;
  --orange:#f5b345;
  --ink:#333333;
  --dark:#353535;
  --footer:#1f1f1f;
  --light:#ebebeb;
  --grey:#9d9d9d;
  --white:#ffffff;
  --head:"Questrial", "Century Gothic", sans-serif;
  --body:"Open Sans", Arial, sans-serif;
}
*{box-sizing:border-box;margin:0;padding:0}
html,body{width:1200px;height:3015px;overflow:hidden}
body{position:relative;background:var(--light);font-family:var(--body);color:var(--ink)}
.abs{position:absolute}

/* hero */
.hero{left:0;top:0;width:1200px;height:740px;background:linear-gradient(100deg,#6a5a48 0%,#8a7a66 35%,#4f4536 60%,#2f3a2c 100%)}
.site-header{left:60px;top:0;width:1076px;height:115px;display:flex}
.brand{width:255px;height:115px;background:var(--white);display:flex;align-items:center;padding-left:22px;gap:12px}
.brand-dot{width:44px;height:44px;border-radius:50%;background:var(--teal)}
.brand-name{font-family:var(--head);font-size:40px;color:#555;line-height:1}
.brand-tag{font-family:var(--head);font-size:12px;color:#555;margin-top:2px}
.topbar{flex:1;background:var(--teal);color:var(--white);position:relative}
.contact-line{position:absolute;left:30px;top:12px;font-size:12px}
.contact-line span{margin-right:26px}
.lang{position:absolute;right:22px;top:12px;font-size:12px;display:flex;gap:6px;align-items:center}
.flag{width:22px;height:14px;display:inline-block}
.nav{position:absolute;left:30px;top:45px;right:80px;height:70px;border-top:1px solid rgba(255,255,255,.25);display:flex;align-items:center;gap:36px;font-size:12.5px;font-weight:600;text-transform:uppercase}
.search{position:absolute;right:18px;top:66px;width:28px;height:28px;background:rgba(255,255,255,.25);border-radius:3px}
.hero-copy{left:612px;top:175px;width:510px;color:var(--white)}
.hero-copy h1{font-family:var(--head);font-weight:400;font-size:38px;line-height:1.05;text-transform:uppercase}
.hero-copy h1 b{display:block;font-size:58px;font-weight:400}
.hero-copy p{font-size:14px;line-height:1.55;margin-top:22px}
.btn{display:inline-block;border:2px solid currentColor;padding:12px 26px;font-size:13px;font-weight:600;text-transform:uppercase}
.hero-copy .btn{margin-top:26px}

/* welcome */
.welcome{left:74px;top:838px;width:640px}
.welcome h2{font-family:var(--head);font-weight:400;font-size:34px;color:#222}
.welcome p{font-size:13.4px;line-height:1.9;margin-top:16px;color:#555}
.welcome .btn{margin-top:26px;color:#1d6d60;border-color:var(--teal)}
.teacher{left:792px;top:565px;width:333px;height:605px;background:var(--dark);color:var(--white)}
.teacher-photo{width:333px;height:258px;background:linear-gradient(180deg,#d8d8d8,#8e8e8e)}
.teacher h3{font-family:var(--head);font-weight:400;font-size:29px;margin:22px 26px 0}
.teacher p{font-size:13px;line-height:1.9;margin:14px 26px 0;color:#e4e4e4}

/* levels */
.levels{left:0;top:1215px;width:1200px;height:920px;background:var(--teal);color:var(--white)}
.levels h2{position:absolute;left:0;width:1200px;top:60px;text-align:center;font-family:var(--head);font-weight:400;font-size:32px}
.levels .lead{position:absolute;left:0;width:1200px;top:112px;text-align:center;font-size:16px;font-weight:700;line-height:1.5}
.levels-figure{left:140px;top:1385px;width:960px;height:500px;border-radius:6px;background:linear-gradient(180deg,var(--teal-soft) 0%,#5cbf93 55%,#c9b25a 100%)}
.level-code{position:absolute;top:1838px;width:76px;text-align:center;font-family:var(--head);font-size:26px;color:var(--white)}
.level-desc{position:absolute;top:1896px;width:100px;font-size:10.6px;line-height:1.6;text-align:center;color:var(--white)}
.level-group{position:absolute;top:2052px;font-size:10px;font-weight:700;text-align:center;line-height:1.3;color:var(--white)}

/* tutoring */
.screen{left:116px;top:2190px;width:374px;height:310px;background:linear-gradient(180deg,#cfd6dc 0%,#e9eef2 70%,#b9bdc2 100%);border-radius:10px}
.tutoring{left:584px;top:2250px;width:520px}
.tutoring h2{font-family:var(--head);font-weight:400;font-size:32px;color:#222}
.tutoring p{font-size:13.4px;line-height:1.8;margin-top:14px;color:#555}

/* newsletter */
.newsletter{left:0;top:2575px;width:1200px;height:85px;background:var(--teal);color:var(--white)}
.newsletter h4{position:absolute;left:100px;top:26px;font-family:var(--head);font-weight:400;font-size:25px}
.signup{position:absolute;left:392px;top:22px;width:352px;height:40px;background:var(--white);border-radius:20px;overflow:hidden}
.signup span{position:absolute;left:18px;top:11px;font-size:12px;color:var(--grey)}
.signup b{position:absolute;right:0;top:0;width:122px;height:40px;background:#222;border-radius:20px;text-align:center;line-height:40px;font-size:14px;font-family:var(--head)}
.socials{position:absolute;left:860px;top:20px;display:flex;gap:12px}
.socials span{width:42px;height:42px;border:2px solid var(--white);border-radius:50%;font-size:6.5px;display:flex;align-items:center;justify-content:center;text-align:center}

/* footer */
.footer{left:0;top:2660px;width:1200px;height:255px;background:var(--footer);color:#cfcfcf}
.foot-brand{position:absolute;left:150px;top:50px;display:flex;align-items:center;gap:10px}
.foot-brand .brand-dot{width:36px;height:36px}
.foot-brand b{font-family:var(--head);font-weight:400;font-size:40px;color:var(--white)}
.copyright{position:absolute;left:100px;top:178px;width:240px;text-align:center;font-size:11px;line-height:1.6}
.foot-col{position:absolute;top:36px}
.foot-col h5{font-family:var(--head);font-weight:400;font-size:15px;color:var(--white);text-transform:uppercase;margin-bottom:14px}
.foot-col li{list-style:none;font-size:12px;line-height:24px}
.foot-col .item{display:flex;gap:10px;font-size:12px;line-height:1.55;margin-bottom:12px}
.map{left:855px;top:2690px;width:268px;height:188px;border-radius:14px;background:linear-gradient(135deg,#e6e1d2,#cfdcc4 55%,#d9d4c4)}
.payments{left:0;top:2915px;width:1200px;height:100px;background:var(--light);display:flex;justify-content:center;align-items:center;gap:44px;font-family:var(--head);font-size:24px;color:#a9a9a9;padding-left:30px}
</style>
</head>
<body>

<div class="abs hero" role="img" aria-label="Photo of a smiling student working on a laptop in a café"></div>

<header class="abs site-header">
  <div class="brand">
    <span class="brand-dot"></span>
    <div><div class="brand-name">KiLa</div><div class="brand-tag">Solvander learning</div></div>
  </div>
  <div class="topbar">
    <div class="contact-line">
      <span>
        <svg width="10" height="12" viewBox="0 0 10 12"><rect x="1" y="0" width="8" height="12" rx="1.5" fill="#fff"/></svg>
        (800) 1800 555 0142</span>
      <span>
        <svg width="12" height="9" viewBox="0 0 12 9"><rect width="12" height="9" fill="#fff"/><path d="M0 0l6 5 6-5" stroke="#00a990" fill="none"/></svg>
        info@solvanderlearn.com</span>
    </div>
    <div class="lang">Language :
      <svg class="flag" viewBox="0 0 22 14"><rect width="22" height="14" fill="#24357a"/><path d="M0 0L22 14M22 0L0 14" stroke="#fff" stroke-width="3"/><path d="M11 0v14M0 7h22" stroke="#fff" stroke-width="4"/><path d="M11 0v14M0 7h22" stroke="#c8102e" stroke-width="2"/></svg>
      <svg class="flag" viewBox="0 0 22 14"><rect width="22" height="14" fill="#ba0c2f"/><path d="M8 0v14M0 7h22" stroke="#fff" stroke-width="4"/><path d="M8 0v14M0 7h22" stroke="#00205b" stroke-width="2"/></svg>
    </div>
    <nav class="nav">
      <span>Home</span><span>About us</span><span>Services</span><span>Why choose us?</span><span>FAQ</span><span>Contact us</span><span>Terms of use</span>
    </nav>
    <div class="search"></div>
  </div>
</header>

<section class="abs hero-copy">
  <h1>Take the world's best <b>Online courses</b></h1>
  <p>Online school in Norway, offering online courses for expats and other people taking courses in Norwegian and Social Studies, which is mandatory to get permanent residency in Norway.</p>
  <span class="btn">Learn more</span>
</section>

<section class="abs welcome">
  <h2>Welcome to Solvander learning</h2>
  <p>KiLa is an online school offering custom made courses for everyone who want to learn Norwegian. Whether you are living abroad or in Norway, you can learn Norwegian with the online programs. You will also speak to your tutor in Callvio, as part of the course. KiLa is approved by SARN and EMT, and all hours will be credited and counted as part of the mandatory 250 hours or 550 hours Norwegian as well as 50 hours social studies.</p>
  <span class="btn">Learn more</span>
</section>

<aside class="abs teacher">
  <div class="teacher-photo" role="img" aria-label="Black and white portrait of the teacher"></div>
  <h3>Marit Holvenes</h3>
  <p>I am educated a teacher from Fjordvik University College, and I have been teaching Norwegian as a second language for more than 10 years. I have lived abroad in both Canada and Tanzania and I would say I have an international mindset. As a teacher, I am energetic and passionate about my work, and I think that learning the language in the country where you live is the key to success.</p>
</aside>

<section class="abs levels">
  <h2>All Levels A1-C2</h2>
  <p class="lead">The online courses are taught on all levels,<br>fra A1 (beginner) to C2 (proficient).</p>
</section>

<div class="abs levels-figure" role="img" aria-label="Illustration of a young man with a briefcase climbing stairs that rise through six level bars towards an arrow"></div>

<span class="level-code" style="left:314px">A1</span>
<span class="level-code" style="left:432px">A2</span>
<span class="level-code" style="left:545px">B1</span>
<span class="level-code" style="left:661px">B2</span>
<span class="level-code" style="left:778px">C1</span>
<span class="level-code" style="left:894px">C2</span>

<p class="level-desc" style="left:302px">Can Read a very short rehearsed statement - e.g. to introduce a speaker, propose a toast...</p>
<p class="level-desc" style="left:418px">Can give a short, rehearsed, basic presentation on a familiar subject.</p>
<p class="level-desc" style="left:533px">Can give a prepared straightforward presentation on a familiar topic within his/her field.</p>
<p class="level-desc" style="left:649px">Can give a clear, prepared presentation.</p>
<p class="level-desc" style="left:766px">Can give a clear, well-structured presentation of a complex subject.</p>
<p class="level-desc" style="left:882px">Can present a complex topic confidently and articulately to an audience unfamiliar with it.</p>

<svg class="abs" style="left:0;top:2000px" width="1200" height="80" viewBox="0 0 1200 80">
  <g stroke="#fff" stroke-opacity=".6" stroke-width="1.5" fill="none">
    <polyline points="356,10 356,66 392,66"/><polyline points="468,10 468,66 432,66"/>
    <polyline points="586,10 586,66 604,66"/><polyline points="700,10 700,66 664,66"/>
    <polyline points="816,10 816,66 840,66"/><polyline points="932,10 932,66 904,66"/>
  </g>
</svg>
<p class="level-group" style="left:382px;width:60px">BASIC<br>USER</p>
<p class="level-group" style="left:584px;width:100px">INDEPENDENT<br>USER</p>
<p class="level-group" style="left:822px;width:100px">PROFICIENT<br>USER</p>

<div class="abs screen" role="img" aria-label="Illustration of a desktop computer with keyboard and mouse showing a video call app"></div>
<section class="abs tutoring">
  <h2>Online Tutoring in Callvio</h2>
  <p>Online tutoring is a great opportunity to learn Norwegian from your own livingroom! All lessons are customized to your needs.</p>
</section>

<section class="abs newsletter">
  <h4>SIGN UP NEWSLETTER!</h4>
  <div class="signup"><span>Email Address</span><b>SEND</b></div>
  <div class="socials"><span>Chatterloom</span><span>Chirpwell</span><span>Plusora</span><span>Vidmora</span></div>
</section>

<footer class="abs footer">
  <div class="foot-brand"><span class="brand-dot"></span><b>KiLa</b></div>
  <p class="copyright">Copyright © 2015 Solvander learning<br>Terms of Use | Sitemap</p>
  <div class="foot-col" style="left:404px">
    <h5>Quick links</h5>
    <ul><li>Home</li><li>About Us</li><li>Services</li><li>Why choose us?</li><li>FAQ</li><li>Contact Us</li></ul>
  </div>
  <div class="foot-col" style="left:610px;width:200px">
    <h5>Contact info</h5>
    <div class="item"><svg width="12" height="16" viewBox="0 0 12 16"><path d="M6 0a6 6 0 0 1 6 6c0 4-6 10-6 10S0 10 0 6a6 6 0 0 1 6-6z" fill="#cfcfcf"/><circle cx="6" cy="6" r="2.2" fill="#1f1f1f"/></svg><span>228, Lorem ipsum dolor<br>dosis amet - 885895</span></div>
    <div class="item"><svg width="12" height="16" viewBox="0 0 12 16"><rect x="1" y="0" width="10" height="16" rx="2" fill="#cfcfcf"/></svg><span>Call Us<br>(800) 1800 555 0142</span></div>
    <div class="item"><svg width="14" height="11" viewBox="0 0 14 11"><rect width="14" height="11" fill="#cfcfcf"/><path d="M0 0l7 6 7-6" stroke="#1f1f1f" fill="none"/></svg><span>Email Us<br>info@solvanderlearn.com</span></div>
  </div>
</footer>
<div class="abs map" role="img" aria-label="Street map showing the school location"></div>

<div class="abs payments"><span>Coinlyx</span><span>Corda</span><span>Bluvex</span><span>Frensa</span></div>

</body>
</html>
```